E brochure for company overview

We need a brochure for a company overview that will be sent to potential new clients. We are uploading a file with all the content that needs to be included inside of the brochure. We need this content to be displayed in a professional, neat, and creative way. The file has a Spanish and English version so we need two versions of the brochure in each language. *This brochure will be viewed digitally and it will not be printed, thus it does not need a cover page*. We included our company logo (Parvolux) Please utilize this in your design.

```html
<!DOCTYPE html>
<html lang="en">
<head>
<meta charset="utf-8">
<title>Parvolux – Company Overview</title>
<link href="https://fonts.googleapis.com/css2?family=Montserrat:wght@500;700;800;900&family=Open+Sans:wght@400;600;700&display=swap" rel="stylesheet">
<style>
  :root{
    --red:#d7262c;
    --red-dark:#b51d22;
    --orange:#f07a22;
    --navy:#1f2a44;
    --ink:#333a45;
    --grey:#6b7280;
    --line:#d9dce1;
    --tile:#eef0f3;
    --footer:#2b2f36;
    --white:#ffffff;
  }
  *{margin:0;padding:0;box-sizing:border-box}
  html,body{width:1200px;height:2340px;overflow:hidden;background:var(--white)}
  body{font-family:"Open Sans",Arial,sans-serif;color:var(--ink)}
  .sheet{position:relative;width:1200px;height:2340px;overflow:hidden;background:var(--white)}

  .brand{position:absolute;left:70px;top:70px;display:flex;align-items:center;gap:18px}
  .brand-dot{width:62px;height:62px;border-radius:50%;background:var(--red)}
  .brand-name{font-family:"Montserrat",Arial,sans-serif;font-weight:800;font-size:52px;color:var(--navy);letter-spacing:1px;line-height:1}
  .brand-tag{font-family:"Montserrat",Arial,sans-serif;font-weight:600;font-size:15px;color:var(--grey);letter-spacing:2px;margin-top:6px}

  .hero-visual{position:absolute;right:-150px;top:-80px;width:620px;height:620px;border-radius:50%;
    background:radial-gradient(circle at 45% 50%,#e9eef5 0%,#9fb4cc 30%,#3c5677 52%,var(--orange) 66%,var(--red) 80%,#7a1014 100%)}

  .history{position:absolute;left:70px;top:400px;font-family:"Montserrat",Arial,sans-serif;font-weight:900;font-size:84px;line-height:1.05;color:var(--navy)}
  .history .accent{color:var(--red)}

  .intro{position:absolute;left:70px;right:70px;top:780px;display:grid;grid-template-columns:1fr 1fr;gap:80px}
  .intro-head{display:flex;align-items:center;gap:18px;margin-bottom:26px}
  .intro-title{font-family:"Montserrat",Arial,sans-serif;font-weight:800;font-size:44px;color:var(--navy)}
  .intro-text{font-size:25px;line-height:1.5;color:var(--red-dark)}

  .services{position:absolute;left:70px;right:70px;top:1300px;height:620px;border:3px solid var(--line);border-radius:14px;padding:90px 50px 0}
  .services-label{position:absolute;left:50%;top:-32px;transform:translateX(-50%);background:var(--red);color:var(--white);
    font-family:"Montserrat",Arial,sans-serif;font-weight:800;font-size:36px;padding:10px 44px;border-radius:8px;white-space:nowrap}
  .services-text{font-size:27px;line-height:1.5;color:var(--red-dark);margin-bottom:70px}
  .values{display:flex;justify-content:space-between}
  .value{width:170px;text-align:center}
  .value-icon{width:130px;height:130px;margin:0 auto 18px;border:5px solid var(--red);border-radius:50%;display:flex;align-items:center;justify-content:center}
  .value-name{font-family:"Montserrat",Arial,sans-serif;font-weight:700;font-size:21px;color:var(--navy);line-height:1.2}

  .partners{position:absolute;left:70px;right:70px;top:1990px;display:grid;grid-template-columns:repeat(4,1fr);gap:24px}
  .partner{height:120px;background:var(--tile);display:flex;align-items:center;justify-content:center;
    font-family:"Montserrat",Arial,sans-serif;font-weight:700;font-size:30px;color:var(--navy)}

  .footer{position:absolute;left:0;right:0;bottom:0;height:150px;display:flex}
  .footer-phone{width:440px;background:var(--red);color:var(--white);display:flex;align-items:center;justify-content:center;gap:18px;
    font-family:"Montserrat",Arial,sans-serif;font-weight:800;font-size:42px}
  .footer-contact{flex:1;background:var(--footer);color:var(--white);display:flex;align-items:center;justify-content:space-around;font-size:24px}
</style>
</head>
<body>
<div class="sheet">

  <div class="hero-visual" role="img" aria-label="Circular technology photo framed by red and orange sweeping arcs"></div>

  <header class="brand">
    <span class="brand-dot"></span>
    <div>
      <div class="brand-name">PARVOLUX</div>
      <div class="brand-tag">IT CONSULTING AND SERVICES</div>
    </div>
  </header>

  <h1 class="history">HISTORY:<br><span class="accent">PARVOLUX</span><br>INITIATES ON 2006</h1>

  <section class="intro">
    <div class="intro-col">
      <div class="intro-head">
        <svg width="60" height="60" viewBox="0 0 60 60" aria-hidden="true">
          <circle cx="30" cy="30" r="26" fill="none" stroke="#1f2a44" stroke-width="5"/>
          <circle cx="30" cy="30" r="15" fill="none" stroke="#d7262c" stroke-width="5"/>
          <circle cx="30" cy="30" r="5" fill="#1f2a44"/>
        </svg>
        <h2 class="intro-title">MISSION</h2>
      </div>
      <p class="intro-text">Providing our customers with the best human and technological resources with the clear objective of providing effective solutions using best industry practices.</p>
    </div>
    <div class="intro-col">
      <div class="intro-head">
        <svg width="66" height="60" viewBox="0 0 66 60" aria-hidden="true">
          <path d="M4 30 Q33 2 62 30 Q33 58 4 30Z" fill="none" stroke="#1f2a44" stroke-width="5"/>
          <circle cx="33" cy="30" r="11" fill="#d7262c"/>
        </svg>
        <h2 class="intro-title">VISION:</h2>
      </div>
      <p class="intro-text">To be recognized by our customers as an important Company in the Dominican Republic in the area of security and other structures and achieve presence through out the Caribbean and Central America.</p>
    </div>
  </section>

  <section class="services">
    <div class="services-label">OUR SERVICES</div>
    <p class="services-text">Service Management, Security of Information, Custom development, Device and network monitoring, Devops, API management, Staffing Values</p>
    <div class="values">
      <div class="value">
        <div class="value-icon"><svg width="64" height="64" viewBox="0 0 64 64" aria-hidden="true"><path d="M32 4 L56 14 V32 C56 46 45 56 32 60 C19 56 8 46 8 32 V14Z" fill="#1f2a44"/><path d="M21 32 L29 40 L44 24" fill="none" stroke="#fff" stroke-width="5"/></svg></div>
        <div class="value-name">INTEGRITY</div>
      </div>
      <div class="value">
        <div class="value-icon"><svg width="64" height="64" viewBox="0 0 64 64" aria-hidden="true"><circle cx="32" cy="26" r="18" fill="#1f2a44"/><rect x="24" y="44" width="16" height="12" rx="2" fill="#d7262c"/></svg></div>
        <div class="value-name">CREATIVITY</div>
      </div>
      <div class="value">
        <div class="value-icon"><svg width="70" height="64" viewBox="0 0 70 64" aria-hidden="true"><circle cx="18" cy="22" r="9" fill="#d7262c"/><circle cx="52" cy="22" r="9" fill="#d7262c"/><circle cx="35" cy="18" r="11" fill="#1f2a44"/><path d="M16 56 C16 40 54 40 54 56Z" fill="#1f2a44"/></svg></div>
        <div class="value-name">TEAM WORK</div>
      </div>
      <div class="value">
        <div class="value-icon"><svg width="64" height="64" viewBox="0 0 64 64" aria-hidden="true"><circle cx="32" cy="32" r="26" fill="none" stroke="#1f2a44" stroke-width="5"/><path d="M20 36 Q32 48 44 36" fill="none" stroke="#d7262c" stroke-width="5"/><circle cx="23" cy="25" r="4" fill="#1f2a44"/><circle cx="41" cy="25" r="4" fill="#1f2a44"/></svg></div>
        <div class="value-name">POSITIVE ATTITUDE</div>
      </div>
      <div class="value">
        <div class="value-icon"><svg width="64" height="64" viewBox="0 0 64 64" aria-hidden="true"><rect x="10" y="8" width="44" height="50" rx="4" fill="#1f2a44"/><path d="M20 24 H44 M20 34 H44 M20 44 H36" stroke="#fff" stroke-width="4"/></svg></div>
        <div class="value-name">COMMITMENT</div>
      </div>
    </div>
  </section>

  <section class="partners">
    <div class="partner">Northgate</div>
    <div class="partner">Kelvora</div>
    <div class="partner">Tessaro</div>
    <div class="partner">Flowline</div>
  </section>

  <footer class="footer">
    <div class="footer-phone">
      <svg width="40" height="40" viewBox="0 0 40 40" aria-hidden="true"><path d="M9 3 L16 3 L19 12 L14 16 C17 22 20 25 25 27 L29 22 L38 25 L38 32 C38 35 35 38 32 37 C17 34 6 23 3 9 C2 6 5 3 9 3Z" fill="#fff"/></svg>
      809 555 0142
    </div>
    <div class="footer-contact">
      <span>info@parvolux.com</span>
      <span>www.parvolux.com.do</span>
    </div>
  </footer>

</div>
</body>
</html>
```